2 Stellenanzeigenbanner für Personaldienstleister zur Werbung auf Promotion-Jobplattform
Die Qualität der Arbeiten war sehr gut. Die Kommunikation mit dem Designer klappte hervorragend. Wir können eine Zusammenarbeit absolut empfehlen!
Zielgruppe
Unser Unternehmen ist primär im Bereich der personalgestützten Absatzförderung am Point of Sale (PoS) mit Schwerpunkt Sales Promotion tätig. Die Zielgruppe der Banner als einzusetzende Werbemittel besteht in erster Linie aus Freiberuflern aus den Bereichen Verkauf und Promotion, die als Markenbotschafter und Fachberater im Auftrag unserer Kunden an den Verkaufspunkten agieren.
Aufgabenstellung
Zur Veröffentlichung auf einer bekannten Promotion-Jobplattform müssen 2 statische Banner in den Formaten 1) 160 x 600 und 2) 468 x 60 erstellt werden, die zu einer Stellenausschreibung führen. Die Banner müssen das offizielle Logo der Agentur sowie die Unternehmensfarben (Rot & Blau) beinhalten und gemeinsam ein einheitliches Design bilden. Die zu verwendenden Textinhalte finden sich in den Anhängen "Text 1" und "Text 2", können vom Designer aber frei angepasst werden.

```html
<!DOCTYPE html>
<html lang="de">
<head>
<meta charset="utf-8">
<title>Standwerk – Stellenbanner</title>
<link rel="stylesheet" href="https://fonts.googleapis.com/css2?family=Oswald:wght@500;700&family=Open+Sans:wght@700;800&display=swap">
<style>
  :root {
    --page-bg: #9dbfdc;
    --navy: #0f5586;
    --blue: #2a7db6;
    --blue-light: #5fb2e0;
    --red: #d3121b;
    --wine: #8c1634;
    --white: #ffffff;
    --panel-grey: #eeeeee;
    --suit: #3b3f86;
  }
  * { box-sizing: border-box; margin: 0; padding: 0; }
  html, body { width: 880px; height: 1200px; overflow: hidden; }
  body {
    position: relative;
    background: var(--page-bg);
    font-family: "Oswald", "Arial Narrow", sans-serif;
  }

  /* ---------- Skyscraper 160x600 ---------- */
  .skyscraper {
    position: absolute; left: 67px; top: 48px;
    width: 258px; height: 960px;
    overflow: hidden;
    box-shadow: 0 2px 6px rgba(0,0,0,.25);
  }
  .sky-head {
    position: absolute; left: 0; top: 0; width: 100%; height: 264px;
    background: var(--white);
  }
  .sky-head .top-band {
    position: absolute; left: 0; top: 0; width: 100%; height: 30px;
    background: var(--navy);
  }
  .sky-head .brand-name {
    position: absolute; left: 0; top: 100px; width: 100%;
    text-align: center; font-weight: 700; font-size: 38px;
    color: var(--navy); letter-spacing: 1px; line-height: 1.2;
  }
  .sky-head .claim {
    position: absolute; left: 0; top: 180px; width: 100%;
    text-align: center; font-weight: 700; font-size: 42px;
    color: var(--wine); letter-spacing: .5px; line-height: 1;
  }

  .sky-stage {
    position: absolute; left: 0; top: 264px; width: 100%; height: 440px;
    background: linear-gradient(180deg, var(--blue) 0%, var(--blue-light) 100%);
    overflow: hidden;
  }
  .sky-stage .stripe {
    position: absolute; left: 0; top: 0; width: 100%; height: 170px;
  }
  .sky-stage .apply {
    position: absolute; left: 16px; top: 40px; width: 230px;
    transform: rotate(-11deg); transform-origin: left top;
    color: var(--red); font-weight: 700; line-height: 1;
    text-align: center;
  }
  .apply .big { display: block; font-size: 46px; letter-spacing: 2px; }
  .apply .small { display: block; font-size: 30px; letter-spacing: 2px; margin-top: 6px; }
  .sky-stage .figure-area {
    position: absolute; left: 0; top: 150px; width: 100%; height: 290px;
    background: linear-gradient(180deg, #7cc7ea 0%, #4b8fc9 55%, var(--suit) 100%);
  }

  .sky-copy {
    position: absolute; left: 0; top: 704px; width: 100%; height: 192px;
    background: var(--panel-grey);
    padding: 10px 12px 0 10px;
    font-weight: 700; line-height: 1.08;
  }
  .sky-copy .role { color: var(--red); font-size: 35px; letter-spacing: .5px; }
  .sky-copy .wanted {
    color: var(--navy); font-size: 42px; text-align: right; letter-spacing: 1px;
  }
  .sky-foot {
    position: absolute; left: 0; top: 896px; width: 100%; height: 64px;
    background: var(--navy);
    color: var(--white);
    font-family: "Open Sans", Arial, sans-serif; font-weight: 700;
    font-size: 13px; line-height: 1.45; text-align: center;
    padding-top: 14px;
  }

  /* ---------- Full banner 468x60 ---------- */
  .leaderboard {
    position: absolute; left: 67px; top: 1056px;
    width: 746px; height: 94px;
    background: var(--white);
    overflow: hidden;
    box-shadow: 0 2px 6px rgba(0,0,0,.25);
  }
  .lb-panel {
    position: absolute; left: 58px; top: 0; width: 440px; height: 100%;
    background: linear-gradient(90deg, var(--navy) 0%, var(--blue) 100%);
  }
  .lb-panel .copy {
    position: absolute; left: 18px; top: 7px; width: 230px;
    color: var(--white); font-weight: 700; font-size: 22px;
    line-height: 1.02; text-align: center; letter-spacing: .5px;
  }
  .lb-panel .figure-area {
    position: absolute; left: 250px; top: 0; width: 120px; height: 100%;
    background: linear-gradient(180deg, #7cc7ea 0%, #4b8fc9 60%, var(--suit) 100%);
  }
  .lb-stripe {
    position: absolute; left: 0; top: 0; width: 100%; height: 100%;
  }
  .lb-apply {
    position: absolute; left: 462px; top: 22px; width: 140px;
    transform: rotate(-11deg);
    color: var(--red); font-weight: 700; line-height: 1; text-align: center;
  }
  .lb-apply .big { display: block; font-size: 26px; letter-spacing: 1px; }
  .lb-apply .small { display: block; font-size: 18px; letter-spacing: 1px; margin-top: 2px; }
  .lb-brand {
    position: absolute; left: 606px; top: 16px; width: 134px; text-align: center;
  }
  .lb-brand .brand-name {
    color: var(--navy); font-weight: 700; font-size: 26px; line-height: 1.1;
    white-space: nowrap;
  }
  .lb-brand .tagline {
    color: var(--red); font-family: "Open Sans", Arial, sans-serif;
    font-weight: 800; font-size: 8.5px; line-height: 1.4; margin-top: 4px;
    white-space: nowrap;
  }
</style>
</head>
<body>

<section class="skyscraper" aria-label="Stellenbanner hoch">
  <header class="sky-head">
    <div class="top-band"></div>
    <div class="brand-name">STANDWERK</div>
    <div class="claim">SUCHT DICH!</div>
  </header>

  <div class="sky-stage">
    <div class="figure-area" role="img" aria-label="Illustration: Mann im Anzug schaut durch ein Fernglas"></div>
    <svg class="stripe" viewBox="0 0 258 170" preserveAspectRatio="none" aria-hidden="true">
      <polygon points="0,58 258,8 258,116 0,166" fill="var(--white)"/>
      <polygon points="0,94 258,44 258,48 0,98" fill="var(--blue)"/>
    </svg>
    <div class="apply">
      <span class="big">SCHNELL</span>
      <span class="small">BEWERBEN</span>
    </div>
  </div>

  <div class="sky-copy">
    <div class="role">SALES<br>PROMOTER &amp;<br>FACHARBEITER</div>
    <div class="wanted">GESUCHT!</div>
  </div>

  <footer class="sky-foot">FÜR MEHR<br>PROFESSIONALITÄT AM POS</footer>
</section>

<section class="leaderboard" aria-label="Stellenbanner quer">
  <div class="lb-panel">
    <div class="copy">SALESPROMOTER<br>&amp; FACHARBEITER<br>WIR SUCHEN DICH!</div>
    <div class="figure-area" role="img" aria-label="Illustration: Mann im Anzug schaut durch ein Fernglas"></div>
  </div>
  <svg class="lb-stripe" viewBox="0 0 746 94" preserveAspectRatio="none" aria-hidden="true">
    <polygon points="448,94 498,0 746,0 746,94" fill="var(--white)"/>
    <polygon points="600,0 606,0 566,94 560,94" fill="var(--blue)"/>
  </svg>
  <div class="lb-apply">
    <span class="big">SCHNELL</span>
    <span class="small">BEWERBEN &gt;</span>
  </div>
  <div class="lb-brand">
    <div class="brand-name">STANDWERK</div>
    <div class="tagline">FÜR MEHR<br>PROFESSIONALITÄT AM POS</div>
  </div>
</section>

</body>
</html>
```